Oil and gas industry project solutions company needs professional cards with Canadian aboriginal fee

We are a aboriginally owned company that is focused on Project Planning, Management, Inspection & Consulting for Canada's Petroleum Industry. We have a logo that we would like to incorporate into a professional looking business card. We are professionals that offer services from project inception to completion.

Target Market(s)

Major industry leaders like NorvaLine, Brisk, Vorkantrel, Pelquist etc.

Industry/Entity Type

Industry

Contact Information for Business Card

Milo Rensford
milo@orvelpike.ca
250 555 0187

Requirements
Must have
• OrvelPike Inc. logo.
• Address is: RR4, Site2, Comp17 Fort St. John, BC V9X 2K3 Traditional Territory of the Treaty 8 People
• Colors that are in logo
• Banner or picture on back
• Ability to put different names and contacts
• Website: orvelpike.ca
• "Project Planning, Management, Inspection & Consulting for Canada's Petroleum Industry"

```html
<!DOCTYPE html>
<html lang="en">
<head>
<meta charset="utf-8">
<title>OrvelPike Inc. — Business Cards</title>
<link href="https://fonts.googleapis.com/css2?family=Open+Sans:wght@400;600;700&display=swap" rel="stylesheet">
<style>
  :root {
    --bg: #e9e6e1;
    --charcoal: #3b3b3d;
    --charcoal-soft: #4a4a4c;
    --white: #ffffff;
    --green: #7cc242;
    --blue: #4a6fb5;
    --navy: #34459a;
    --grey-text: #d9d9d9;
    --photo-a: #6f8d5a;
    --photo-b: #a9b8c4;
  }
  * { box-sizing: border-box; margin: 0; padding: 0; }
  html, body { width: 1200px; height: 800px; overflow: hidden; }
  body {
    background: var(--bg);
    font-family: "Open Sans", Arial, sans-serif;
    position: relative;
  }

  /* ---------- Back card (portrait) ---------- */
  .card-back {
    position: absolute;
    left: 90px; top: 110px;
    width: 340px; height: 580px;
    background: var(--charcoal-soft);
    box-shadow: 0 10px 30px rgba(0,0,0,.25);
    overflow: hidden;
  }
  .card-back .wordmark {
    position: absolute; top: 26px; left: 0; right: 0;
    text-align: center;
    color: var(--grey-text);
    font-weight: 600;
    font-size: 26px;
    letter-spacing: .5px;
  }
  .card-back .rule {
    position: absolute; top: 70px; left: 90px; right: 90px;
    height: 1px; background: var(--grey-text); opacity: .6;
  }
  .card-back .photo {
    position: absolute; top: 95px; left: 55px;
    width: 230px; height: 330px;
    border-radius: 115px 115px 115px 115px / 140px 140px 90px 90px;
    background: linear-gradient(170deg, var(--photo-b) 0%, #8c9aa0 40%, var(--photo-a) 100%);
  }
  .card-back .stripe {
    position: absolute; left: 0; right: 0; top: 455px;
    height: 6px; background: var(--blue);
  }
  .card-back .band {
    position: absolute; left: 0; right: 0; top: 461px; bottom: 0;
    background: var(--green);
    color: var(--white);
    text-align: center;
    padding-top: 20px;
    font-size: 16px;
    line-height: 26px;
  }
  .band .dot {
    display: inline-block; width: 6px; height: 6px; border-radius: 50%;
    background: var(--white); vertical-align: middle; margin: 0 4px;
  }

  /* ---------- Front card (landscape) ---------- */
  .card-front {
    position: absolute;
    left: 510px; top: 230px;
    width: 600px; height: 340px;
    box-shadow: 0 10px 30px rgba(0,0,0,.25);
    overflow: hidden;
  }
  .card-front .shapes { position: absolute; inset: 0; }
  .card-front .brand {
    position: absolute; top: 40px; right: 30px;
    display: flex; align-items: center; gap: 12px;
  }
  .brand .mark {
    width: 20px; height: 20px; border-radius: 50%; background: var(--green);
  }
  .brand .name {
    color: var(--navy);
    font-weight: 700;
    font-size: 34px;
    letter-spacing: -.5px;
  }
  .card-front .address {
    position: absolute; top: 26px; left: 24px;
    width: 225px;
    color: var(--green);
    font-size: 12px;
    line-height: 17px;
  }
  .card-front .person {
    position: absolute; left: 24px; top: 168px;
  }
  .person .full-name {
    color: var(--green); font-weight: 700; font-size: 22px; letter-spacing: .5px;
  }
  .person .role {
    color: var(--white); font-size: 13px; margin-bottom: 12px;
  }
  .contact-list { list-style: none; }
  .contact-list li {
    display: flex; align-items: center; gap: 10px;
    color: var(--white); font-size: 15px; line-height: 24px;
  }
  .contact-list svg { width: 16px; height: 16px; flex: none; }
</style>
</head>
<body>

  <section class="card-back">
    <div class="wordmark">OrvelPike Inc.</div>
    <div class="rule"></div>
    <div class="photo" role="img" aria-label="Photo of a pipeline inspector in hard hat and safety vest beside a pipeline, with forest behind"></div>
    <div class="stripe"></div>
    <div class="band">
      <p>Project Planning <span class="dot"></span> Management</p>
      <p>Inspection &amp; Consulting</p>
      <p>for Canada's Petroleum Industry</p>
    </div>
  </section>

  <section class="card-front">
    <svg class="shapes" viewBox="0 0 600 340" preserveAspectRatio="none">
      <rect width="600" height="340" fill="var(--charcoal)"/>
      <path d="M600,265 C500,175 400,138 320,120 C285,110 265,60 258,0 H600 Z" fill="var(--blue)"/>
      <path d="M600,248 C500,160 400,124 325,106 C292,97 277,55 271,0 H600 Z" fill="var(--white)"/>
    </svg>

    <p class="address">RR4, Site2, Comp17 Fort St. John BC V9X 2K3 Traditional Territory of the Treaty 8 People</p>

    <div class="brand">
      <span class="mark"></span>
      <span class="name">OrvelPike Inc.</span>
    </div>

    <div class="person">
      <p class="full-name">MILO RENSFORD</p>
      <p class="role">Director</p>
      <ul class="contact-list">
        <li>
          <svg viewBox="0 0 16 16"><circle cx="8" cy="8" r="8" fill="var(--green)"/><path d="M5 4.5 l2 0 l.6 2 l-1 .8 a5 5 0 0 0 2.1 2.1 l.8-1 l2 .6 l0 2 a1 1 0 0 1-1 1 A7 7 0 0 1 4 5.5 a1 1 0 0 1 1-1z" fill="var(--charcoal)"/></svg>
          250 555 0187
        </li>
        <li>
          <svg viewBox="0 0 16 16"><circle cx="8" cy="8" r="8" fill="var(--green)"/><rect x="4" y="5" width="8" height="6" fill="var(--charcoal)"/><path d="M4 5 L8 8.5 L12 5" stroke="var(--green)" fill="none" stroke-width="1"/></svg>
          milo@orvelpike.ca
        </li>
        <li>
          <svg viewBox="0 0 16 16"><circle cx="8" cy="8" r="8" fill="var(--green)"/><circle cx="8" cy="8" r="4.5" fill="none" stroke="var(--charcoal)" stroke-width="1.2"/><path d="M3.5 8 H12.5 M8 3.5 C6 6 6 10 8 12.5 M8 3.5 C10 6 10 10 8 12.5" stroke="var(--charcoal)" fill="none" stroke-width="1"/></svg>
          orvelpike.ca
        </li>
      </ul>
    </div>
  </section>

</body>
</html>
```